Simple and Approachable Cover for Pet Expo Company Page

Size: 2000 x 430; looking simply for words "Dunmore HR Consulting" and email address "DunmoreHRConsulting@brelvamail.com." This is for a cover photo for a company profile page for the Hollow Oak Expo, where I am a featured speaker on Employee Communications later this month. You can incorporate the attached photo to the left of the banner ad if you wish. The mood I wish to present is approachable, positive and simple.

Target Market(s)

small pet retail business owners

Industry/Entity Type

Pet Shop

Font styles to use
Serif
Sans Serif

Requirements
Must have
• Email address clearly defined/separated. Easy to read.
Nice to have
• I like the picture that I included; subtle pet paw background is also nice
Should not have
• No paid stock images

```html
<!DOCTYPE html>
<html lang="en">
<head>
<meta charset="utf-8">
<title>Dunmore HR Consulting — Cover Banner</title>
<link rel="stylesheet" href="https://fonts.googleapis.com/css2?family=Domine:wght@700&family=Raleway:wght@400&display=swap">
<style>
  :root {
    --page: #ffffff;
    --lime: #a6d62a;
    --lime-light: #c4e66a;
    --lime-soft: #bde357;
    --ink: #111111;
    --photo-sky: #8a9a5e;
    --photo-grass: #7f8d4a;
    --photo-warm: #b89a6a;
  }
  * { margin: 0; padding: 0; box-sizing: border-box; }
  html, body {
    width: 1200px;
    height: 1000px;
    overflow: hidden;
    background: var(--page);
  }
  .cover {
    position: absolute;
    left: 79px;
    top: 389px;
    width: 1040px;
    height: 223px;
    background: var(--lime);
    overflow: hidden;
  }
  .cover__art {
    position: absolute;
    inset: 0;
    width: 100%;
    height: 100%;
  }
  .cover__title {
    position: absolute;
    left: 52px;
    top: 62px;
    font-family: "Domine", Georgia, serif;
    font-weight: 700;
    font-size: 50px;
    line-height: 1;
    color: var(--ink);
    white-space: nowrap;
    letter-spacing: 0.3px;
  }
  .cover__email {
    position: absolute;
    left: 188px;
    top: 130px;
    font-family: "Raleway", Arial, sans-serif;
    font-weight: 400;
    font-size: 27px;
    line-height: 1;
    color: var(--ink);
    white-space: nowrap;
  }
</style>
</head>
<body>
  <section class="cover">
    <svg class="cover__art" viewBox="0 0 1040 223" preserveAspectRatio="none">
      <defs>
        <linearGradient id="photoTone" x1="0" y1="0" x2="0" y2="1">
          <stop offset="0" stop-color="var(--photo-sky)"/>
          <stop offset="0.5" stop-color="var(--photo-warm)"/>
          <stop offset="1" stop-color="var(--photo-grass)"/>
        </linearGradient>
        <radialGradient id="pawGlow" cx="0.5" cy="0.5" r="0.5">
          <stop offset="0" stop-color="var(--lime-soft)" stop-opacity="0.9"/>
          <stop offset="0.7" stop-color="var(--lime-soft)" stop-opacity="0.5"/>
          <stop offset="1" stop-color="var(--lime-soft)" stop-opacity="0"/>
        </radialGradient>
      </defs>
      <g class="cover__paw-pattern" role="img" aria-label="Subtle light green paw-print pattern in the background">
        <ellipse cx="210" cy="105" rx="100" ry="100" fill="url(#pawGlow)"/>
        <ellipse cx="497" cy="128" rx="100" ry="98" fill="url(#pawGlow)"/>
      </g>
      <polygon class="cover__stripe" points="676,0 681,0 727,223 722,223" fill="var(--lime-light)"/>
      <polygon class="cover__stripe" points="693,0 698,0 747,223 742,223" fill="var(--lime-light)"/>
      <polygon class="cover__photo" points="707,0 1040,0 1040,223 751,223" fill="url(#photoTone)"
        role="img" aria-label="Photo of a smiling couple sitting on the grass in a park with two hound dogs"/>
    </svg>
    <h1 class="cover__title">Dunmore HR Consulting</h1>
    <p class="cover__email">DunmoreHRConsulting@brelvamail.com</p>
  </section>
</body>
</html>
```